pressure washing advertisment

I would like front and back designed post cards. we offer pressure washing services for residential customers. I want to highlight before and after pictures as examples of our more popular services. I would also like to have our email www.bluhavenwashco.example and the facebook and Instagram logo somewhere. you can also include all major credit card logos as acceptable payments. I have attached our logo along with before and after pictures. also feel free to go to my website for any additional information that should be added to the post card. lastly I want a small promotion of $25 off any service somewhere.<br/><br/>Thank you!!

Target Market(s)

homeowners

Industry/Entity Type

Cleaning Service

Font styles to use
Serif
Sans Serif

Colors

Designer to choose colors to be used in the design.

Requirements
Must have
• before and after pictures with website and logo
Nice to have
• clean look that flows

```html
<!DOCTYPE html>
<html lang="en">
<head>
<meta charset="utf-8">
<title>Bluhaven Wash Co – Pressure Washing Postcard</title>
<link href="https://fonts.googleapis.com/css2?family=Roboto+Condensed:wght@700;800;900&family=Archivo:wght@800&display=swap" rel="stylesheet">
<style>
  :root{
    --red:#c8282d;
    --navy:#1d3a6b;
    --white:#ffffff;
    --ink:#111111;
    --paving-dark:#5f5956;
    --paving-mid:#8c8580;
    --paving-light:#b2aca6;
    --siding:#9fb1a0;
    --siding-clean:#b8c9b6;
  }
  html,body{margin:0;padding:0;overflow:hidden;background:#fff;}
  .postcard{
    position:relative;width:1200px;height:857px;overflow:hidden;
    font-family:"Roboto Condensed","Arial Narrow",sans-serif;color:var(--white);
  }
  .paving-photo{
    position:absolute;inset:0 0 143px 0;
    background:
      linear-gradient(90deg,rgba(70,90,60,.55) 0,rgba(70,90,60,0) 160px),
      linear-gradient(180deg,var(--paving-light) 0,var(--paving-mid) 45%,var(--paving-dark) 100%);
  }
  .headline{position:absolute;left:0;top:0;width:1200px;height:714px;}
  .headline text{font-family:"Roboto Condensed","Arial Narrow",sans-serif;font-weight:900;fill:var(--white);}
  .headline .services{font-weight:700;font-size:27px;}
  .headline .cta{font-weight:800;}
  .photo{position:absolute;border:4px solid var(--white);box-sizing:border-box;}
  .photo-before{left:81px;top:386px;width:409px;height:285px;
    background:linear-gradient(180deg,#c9d2d4 0,#8fa08e 20%,var(--siding) 60%,#6f806d 100%);}
  .photo-after{left:452px;top:252px;width:410px;height:286px;
    background:linear-gradient(180deg,#dfe5e6 0,var(--siding-clean) 18%,#a9bca8 80%,#7d8d7b 100%);}
  .benefit{position:absolute;display:flex;align-items:flex-start;gap:10px;
    font-weight:800;font-size:26px;line-height:35px;text-transform:uppercase;white-space:nowrap;}
  .benefit svg{margin-top:12px;flex:none;}
  .follow{position:absolute;left:649px;top:657px;display:flex;align-items:center;gap:10px;
    font-weight:700;font-size:30px;white-space:nowrap;}
  .follow .dot{width:42px;height:42px;border-radius:50%;background:rgba(255,255,255,.85);}
  .follow .handle{margin-left:8px;}
  .contact-band{
    position:absolute;left:0;top:714px;width:1200px;height:143px;box-sizing:border-box;
    background:var(--white);border:5px solid var(--navy);
  }
  .brand{position:absolute;left:38px;top:30px;color:var(--navy);
    font-family:"Archivo",Arial,sans-serif;font-weight:800;font-size:30px;line-height:36px;}
  .contact-copy{position:absolute;left:0;top:0;width:1200px;height:143px;}
  .contact-copy .lead{font-family:"Archivo",Arial,sans-serif;font-weight:800;fill:var(--ink);font-size:32px;}
  .contact-copy .lines{font-family:"Roboto Condensed","Arial Narrow",sans-serif;font-weight:700;fill:var(--red);font-size:39px;}
</style>
</head>
<body>
<main class="postcard">
  <div class="paving-photo" role="img" aria-label="Photo of a clean brick block-paved driveway with garden rocks and shrubs at the left edge"></div>

  <div class="photo photo-after" role="img" aria-label="After photo: clean light green vinyl siding on the side of a house"></div>
  <div class="photo photo-before" role="img" aria-label="Before photo: mossy, stained green vinyl siding on the side of a house"></div>

  <svg class="headline" viewBox="0 0 1200 714">
    <polygon points="866,0 1200,0 1200,238" fill="var(--red)"/>
    <g transform="translate(1122 86) rotate(38)">
      <text x="14" y="-40" font-size="46" text-anchor="middle">OFF</text>
      <text x="-4" y="44" font-size="90" text-anchor="middle">$25</text>
    </g>
    <text x="29" y="122" font-size="140" textLength="571" lengthAdjust="spacingAndGlyphs">PRESSURE</text>
    <text x="29" y="231" font-size="140" textLength="503" lengthAdjust="spacingAndGlyphs">WASHING</text>
    <text class="services" x="557" y="157" textLength="296" lengthAdjust="spacingAndGlyphs">DRIVEWAYS, PATIOS,</text>
    <text class="services" x="557" y="195" textLength="348" lengthAdjust="spacingAndGlyphs">BRICK &amp; BLOCK PAVING,</text>
    <text class="services" x="557" y="233" textLength="390" lengthAdjust="spacingAndGlyphs">WALLS, STEPS, PATHS, DECKING</text>
    <text class="cta" x="543" y="636" font-size="104" textLength="588" lengthAdjust="spacingAndGlyphs">CALL NOW TODAY!</text>
  </svg>

  <div class="benefit" style="left:157px;top:275px;">
    <svg width="30" height="26" viewBox="0 0 30 26"><path d="M2 14 L11 23 L28 2" fill="none" stroke="var(--red)" stroke-width="4"/></svg>
    <span>Improves<br>Appearance</span>
  </div>
  <div class="benefit" style="left:885px;top:275px;">
    <svg width="30" height="26" viewBox="0 0 30 26"><path d="M2 14 L11 23 L28 2" fill="none" stroke="var(--red)" stroke-width="4"/></svg>
    <span>Reduces<br>Maintenance</span>
  </div>
  <div class="benefit" style="left:885px;top:363px;">
    <svg width="30" height="26" viewBox="0 0 30 26"><path d="M2 14 L11 23 L28 2" fill="none" stroke="var(--red)" stroke-width="4"/></svg>
    <span>Have it look<br>new again</span>
  </div>
  <div class="benefit" style="left:885px;top:451px;">
    <svg width="30" height="26" viewBox="0 0 30 26"><path d="M2 14 L11 23 L28 2" fill="none" stroke="var(--red)" stroke-width="4"/></svg>
    <span>Removes<br>moss &amp; lichen</span>
  </div>

  <div class="follow">
    <span>Follow us</span>
    <span class="dot" aria-hidden="true"></span>
    <span class="dot" aria-hidden="true"></span>
    <span class="handle">bluhavenwashco</span>
  </div>

  <footer class="contact-band">
    <div class="brand">BLUHAVEN<br>WASH CO LLC</div>
    <svg class="contact-copy" viewBox="0 0 1200 143">
      <text class="lead" x="806" y="40" text-anchor="middle" textLength="640" lengthAdjust="spacingAndGlyphs">FOR ALL YOUR PRESSURE CLEANING</text>
      <text class="lead" x="806" y="72" text-anchor="middle" textLength="372" lengthAdjust="spacingAndGlyphs">REQUIREMENTS CALL</text>
      <text class="lines" x="450" y="116" textLength="722" lengthAdjust="spacingAndGlyphs">01632 960 482 or email us: dana@bluhavenwashco.example</text>
    </svg>
  </footer>
</main>
</body>
</html>
```